Homepage design competition to choose a designer for $1500 full website for a Small Animal Veterinar

We are running a homepage design competition to choose a designer who will later code an entire website. Please note, this competition is only for the front page design. There will be an additional payment of $1500 (Australian $AUD) for the complete website design including coding payment.

Front Page: First we need a front page design for our companion animal veterinary hospital. I will use the frontpage design competition to choose a designer for the full website.
Marlow Vet Clinic is a companion animal veterinary hospital in Singleton NSW. We provide veterinary medical and surgical treatment for dogs, cats, rabbits, birds and reptiles. Mostly dogs and cats.
Our reception is a 120 year old church and the hospital is 6 years old and custom built.
I want the site to be amazing. The sort of thing that could win prizes. The front page should be simple, fun and engaging whilst maintaining a strong sense of professionalism. Simple and elegant visual effects with subtle movement. The winning design will show originality.
Our main demographic is women aged 25 to 44 years old. We are a coal mining town. Most of our money comes from coal miners wives.
The front page must display our phone number and link to our facebook page. Otherwise the front page can have anything. The front page should impress new clients and reassure existing clients.
We pride ourselves on following up everything and caring for pets and their people their entire life. Please see our existing (horrible) website for more details about our business. http://www.marlowvetclinic.example/
Incorporate only amazing things from the old website. I hate the old website, so there is probably not much to use. We need something new and amazing.
Fully responsive design.

Characters: We have a logo and animal characters to incorporate into the design. These characters will be used throughout our email and facebook advertising. If they could be used with some movement and sound effects, that would be cool, but nothing too childish or silly.

Live site: please include links to live demo sites if possible.
Please include links to your other work.

Full Website: The successful designer of the frontpage must be able to demonstrate the ability produce a full website. The full website designer will be commissioned after the front page is chosen. We have budgeted for a full website of $1500.
I need to be able to add new articles to the website that will link from email newsletters and facebook, so the full website will need to be something I can modify or add to.
I have a working knowledge of Joomla, Wordpress and html.
The full website will have map, history of the hospital, history of the chapel, links to local services, pet care advice, memorials.
Ideally the winning designer will be able to integrate appointments available with our existing veterinary management software.
Fully responsive design.

Here are some websites that I like:
https://drbexley.example.au/
http://quincepepper.example/
http://www.xn--dorotawelnicka-abc12k.example/
https://www.zov.example.au/
https://www.frisko.example.au/
https://topmowers.example.au/
https://www.redgatecider.example/

Target Market(s)

Women aged 25 to 44 years

Industry/Entity Type

Veterinary

Number of Pages Required

1 page

Font styles to use
Serif
Sans Serif

Requirements
Must have
• Phone number
• Pagebook Link https://www.pagebook.example/marlow.vetclinic?v=wall
• Simplicity
• Originality
• Animal characters-images attached
Nice to have
• Images
• Clean
• Link to live site.
• Links to your other work.
• Demonstrate ability to integrate appointment booking with our veterinary software
Should not have
• Heaps of words
• Complexity

```html
<!DOCTYPE html>
<html lang="en">
<head>
<meta charset="utf-8">
<title>Marlow Vet Clinic – Our Clients</title>
<link href="https://fonts.googleapis.com/css2?family=Raleway:wght@400;500;700;800&display=swap" rel="stylesheet">
<style>
  :root{
    --brown:#5a3a1e;
    --green:#6a8f2e;
    --green-bright:#7aa63a;
    --white:#ffffff;
    --ink:#2b2b2b;
    --muted:#8a8a8a;
    --font:'Raleway', Arial, sans-serif;
  }
  *{box-sizing:border-box;margin:0;padding:0}
  html,body{width:1200px;height:1151px;overflow:hidden;background:var(--white);font-family:var(--font);color:var(--ink)}
  .page{position:relative;width:1200px;height:1151px}

  .clients{position:absolute;left:0;top:0;width:1200px;height:540px;background:var(--brown);overflow:hidden}
  .clients__title{position:absolute;left:560px;width:300px;top:56px;text-align:center;font-size:48px;font-weight:800;color:var(--green-bright);letter-spacing:.5px;white-space:nowrap}
  .clients__rule{position:absolute;left:710px;top:126px;transform:translateX(-50%);display:flex;align-items:center;gap:10px}
  .clients__rule span{display:block;width:44px;height:2px;background:var(--green-bright)}
  .clients__rule i{display:block;width:10px;height:10px;border-radius:50%;background:var(--green-bright)}
  .backdrop{position:absolute;left:640px;top:180px;width:560px;height:340px;background:radial-gradient(ellipse at 60% 45%, #8a6a48 0%, #6e4e2f 45%, rgba(90,58,30,0) 75%)}
  .testimonial{position:absolute;display:flex;gap:26px;align-items:flex-start}
  .testimonial--one{left:50px;top:100px}
  .testimonial--two{left:660px;top:260px}
  .avatar{flex:0 0 120px;width:120px;height:120px;border-radius:50%;border:4px solid var(--white);background:linear-gradient(160deg,#c9b9a3,#7c5e44)}
  .testimonial__body{width:330px;padding-top:18px;color:var(--white)}
  .testimonial__quote{font-size:14px;line-height:1.6;font-weight:400;font-style:italic}
  .testimonial__name{margin-top:14px;font-size:16px;font-weight:700}
  .dots{position:absolute;left:50%;top:480px;transform:translateX(-50%);display:flex;gap:8px}
  .dots span{width:9px;height:9px;border-radius:50%;background:#4e7fa8}
  .dots span.is-active{background:var(--white)}

  .footer{position:absolute;left:0;top:540px;width:1200px;height:480px;background:var(--white)}
  .footer__col{position:absolute;top:60px}
  .footer__heading{font-size:15px;font-weight:700;letter-spacing:1px;color:var(--ink);margin-bottom:22px}
  .brand{left:60px;width:280px}
  .brand__mark{display:flex;align-items:center;gap:10px;margin-bottom:20px}
  .brand__square{flex:0 0 34px;width:34px;height:34px;background:var(--brown)}
  .brand__name{font-size:22px;font-weight:700;color:var(--ink);line-height:1.1}
  .brand__info{font-size:14px;line-height:1.75;color:#444}
  .social{display:flex;gap:14px;margin-top:34px}
  .social a{display:block;width:34px;height:34px;border-radius:50%;background:var(--brown)}
  .info{left:380px;top:90px}
  .info ul{list-style:none}
  .info li{font-size:15px;color:var(--muted);margin-bottom:14px}
  .info li:first-child{color:var(--green)}
  .chirp{left:640px;top:120px;width:220px}
  .widget{border-top:3px solid #222;padding-top:6px;font-size:8px;color:#555;line-height:1.4}
  .widget__title{font-weight:700;font-size:8px;margin-bottom:8px;color:#222}
  .post{display:flex;gap:6px;margin-bottom:12px}
  .post__pic{flex:0 0 14px;height:14px;background:#bbb}
  .post__meta{display:flex;justify-content:space-between;gap:6px}
  .follow{display:inline-block;padding:1px 6px;background:#dfeefa;border-radius:2px;font-size:7px}
  .compose{border:1px solid #ccc;padding:3px 5px;margin-top:4px;width:180px}
  .pagebook{left:900px;top:160px;width:220px}
  .fbbox{border:1px solid #c5c8d0;font-size:8px;color:#444;width:190px}
  .fbbox__head{background:#eef0f5;padding:4px 6px;font-weight:700}
  .fbbox__page{display:flex;gap:6px;padding:6px;align-items:center}
  .fbbox__thumb{width:22px;height:22px;background:var(--brown)}
  .fbbox__page b{color:#3b5998}
  .fbbox__count{padding:0 6px 4px}
  .faces{display:grid;grid-template-columns:repeat(5,1fr);gap:4px 6px;padding:4px 6px}
  .face{text-align:center;font-size:6px}
  .face span{display:block;height:22px;background:#9c8f84;margin-bottom:2px}
  .fbbox__foot{border-top:1px solid #ddd;padding:3px 6px;font-size:7px}

  .bottombar{position:absolute;left:0;top:1020px;width:1200px;height:131px;background:var(--green);display:flex;align-items:center;justify-content:center;color:var(--white);font-size:15px;font-weight:500}
</style>
</head>
<body>
<div class="page">

  <section class="clients">
    <div class="backdrop" role="img" aria-label="Soft photo of a cat resting on a blanket"></div>
    <h2 class="clients__title">Our Clients</h2>
    <div class="clients__rule"><span></span><i></i><span></span></div>

    <article class="testimonial testimonial--one">
      <div class="avatar" role="img" aria-label="Portrait photo of a client"></div>
      <div class="testimonial__body">
        <p class="testimonial__quote">Lorem Ipsum is simply dummy text of the printing and typesetting industry. Lorem Ipsum has been the industry's standard dummy text ever since the 1500s.Lorum ipsum is dummy text.</p>
        <p class="testimonial__name">-Nora Hale</p>
      </div>
    </article>

    <article class="testimonial testimonial--two">
      <div class="avatar" role="img" aria-label="Portrait photo of a client"></div>
      <div class="testimonial__body">
        <p class="testimonial__quote">Lorem Ipsum is simply dummy text of the printing and typesetting industry. Lorem Ipsum has been the industry's standard dummy text ever since the 1500s.Lorum ipsum is dummy text.</p>
        <p class="testimonial__name">-Nora Hale</p>
      </div>
    </article>

    <div class="dots"><span class="is-active"></span><span></span><span></span></div>
  </section>

  <footer class="footer">
    <div class="footer__col brand">
      <div class="brand__mark">
        <div class="brand__square"></div>
        <div class="brand__name">MARLOW VET<br>CLINIC</div>
      </div>
      <p class="brand__info">
        Address:<br>
        27 Quarry Lane,<br>
        Singleton NSW 2330<br>
        Phone: 1-800-5550-132<br>
        E-Mail: hello@marlowvet.example
      </p>
      <div class="social">
        <a href="https://www.pagebook.example/marlow.vetclinic?v=wall" aria-label="Pagebook"></a>
        <a href="#" aria-label="Chirp"></a>
        <a href="#" aria-label="Photo feed"></a>
        <a href="#" aria-label="Circles"></a>
      </div>
    </div>

    <nav class="footer__col info">
      <h3 class="footer__heading">INFORMATION</h3>
      <ul>
        <li>Home</li>
        <li>Search</li>
        <li>Sitemap</li>
        <li>Blog</li>
      </ul>
    </nav>

    <div class="footer__col chirp">
      <h3 class="footer__heading">CHIRP FEED</h3>
      <div class="widget">
        <div class="widget__title">CLINIC ON CHIRP</div>
        <div class="post__meta" style="margin-bottom:6px"><b>Posts</b><span class="follow">Follow</span></div>
        <div class="post">
          <div class="post__pic"></div>
          <div>
            <div class="post__meta"><b>Marlow Clinic @marlowvet</b><span>12 Jan</span></div>
            <div>New puppy class dates are now open for booking</div>
            <div>Expand</div>
          </div>
        </div>
        <div class="post">
          <div class="post__pic"></div>
          <div>
            <div class="post__meta"><b>Marlow Clinic @marlowvet</b><span>9 Jan</span></div>
            <div>Weekend hours extended for the holidays</div>
            <div>Expand</div>
          </div>
        </div>
        <div class="compose">Post to @marlowvet</div>
      </div>
    </div>

    <div class="footer__col pagebook">
      <h3 class="footer__heading">PAGEBOOK.</h3>
      <div class="fbbox">
        <div class="fbbox__head">Find us on Pagebook</div>
        <div class="fbbox__page">
          <div class="fbbox__thumb" role="img" aria-label="Page thumbnail"></div>
          <div><b>Marlow Vet Clinic</b><br>You like this. Unlike</div>
        </div>
        <div class="fbbox__count">36 people like Marlow Vet Clinic</div>
        <div class="faces" role="img" aria-label="Thumbnails of page followers">
          <div class="face"><span></span>Anna</div>
          <div class="face"><span></span>Ben</div>
          <div class="face"><span></span>Cara</div>
          <div class="face"><span></span>Dean</div>
          <div class="face"><span></span>Ella</div>
          <div class="face"><span></span>Finn</div>
          <div class="face"><span></span>Gus</div>
          <div class="face"><span></span>Hana</div>
          <div class="face"><span></span>Ivy</div>
          <div class="face"><span></span>Jo</div>
        </div>
        <div class="fbbox__foot">Pagebook social plugin</div>
      </div>
    </div>
  </footer>

  <div class="bottombar">©2016 All Right Reserved.Marlowvetclinic</div>
</div>
</body>
</html>
```